New UK IT business
Business cards etc
Project: New UK IT business
New UK IT business - Environment
Creative Brief
Bright & Fun-filled
Cobalt Harvest Limited or Ltd - Gordon Pressey
Director
14 Brindle Lane Oakhurst Trading Park Fenwick Cross Herts HP9 3QL United Kingdom
gord@cobaltharvest-example.com
www.cobaltharvest-example.com
please do one card for Gord Pressey - Director and one for Rosalind Pressey - Director and one for Company - with no name
full colour - simple logo and website address only for the inside of the card i want it to have the fold on the horizontal meaning 55mm down the front with logo and name and address details the back as described above the inside I would like a picture of business people and have the messages of Redundant IT and Computer equipment Business people - corporate business people wanted All UK areas please suggest what you think and design around it thanks I will be available to answer questions when i see some designs for inspiration

```html
<!DOCTYPE html>
<html lang="en">
<head>
<meta charset="utf-8">
<title>Cobalt Harvest – Business Card Concepts</title>
<link href="https://fonts.googleapis.com/css2?family=Arimo:wght@400;700&display=swap" rel="stylesheet">
<style>
  :root {
    --stage-light: #5a5a5a;
    --stage-dark: #1c1c1c;
    --card-grey-light: #f2f2f2;
    --card-grey-mid: #cfcfcf;
    --card-grey-dark: #9a9a9a;
    --paper: #ffffff;
    --green: #5aa51e;
    --green-light: #8cc63f;
    --ink: #333333;
    --photo-dark: #2e2e2e;
    --photo-light: #8a8a8a;
  }
  * { box-sizing: border-box; margin: 0; padding: 0; }
  html, body { width: 1200px; height: 847px; overflow: hidden; }
  body {
    font-family: "Arimo", Arial, sans-serif;
    background: radial-gradient(ellipse at 50% 45%, var(--stage-light) 0%, #3a3a3a 55%, var(--stage-dark) 100%);
    position: relative;
  }
  .spread { position: absolute; display: flex; gap: 6px; }
  .spread--one { left: 42px; top: 91px; height: 399px; }
  .spread--two { left: 615px; top: 91px; height: 399px; }
  .spread--three { left: 330px; top: 510px; height: 302px; }

  .card { height: 100%; display: flex; flex-direction: column; box-shadow: 0 4px 12px rgba(0,0,0,.5); }
  .card--outer { width: 270px; }
  .card--inner { width: 285px; background: var(--paper); }
  .card__half { flex: 1; position: relative; overflow: hidden; }

  /* outer (grey) card */
  .card--outer .card__half {
    background: radial-gradient(ellipse at 50% 50%, var(--card-grey-light) 0%, var(--card-grey-mid) 60%, var(--card-grey-dark) 100%);
  }
  .card--outer .card__half + .card__half { border-top: 1px solid rgba(0,0,0,.12); }
  .badge {
    position: absolute; left: 50%; top: 50%; transform: translate(-50%, -50%);
    display: flex; flex-direction: column; align-items: center; gap: 8px;
  }
  .badge__disc { width: 72px; height: 72px; border-radius: 50%; background: var(--green); }
  .badge__url { font-size: 11px; font-weight: 700; color: var(--ink); transform: rotate(-14deg); letter-spacing: .3px; }
  .spread--three .badge__disc { width: 54px; height: 54px; }
  .spread--three .badge__url { font-size: 9px; }
  .wordmark {
    position: absolute; left: 50%; top: 50%; transform: translate(-50%, -50%);
    display: flex; align-items: center; gap: 6px; white-space: nowrap;
  }
  .wordmark__dot { width: 20px; height: 20px; border-radius: 50%; background: var(--green); }
  .wordmark__name { font-size: 18px; font-weight: 700; color: var(--green); text-transform: uppercase; letter-spacing: .5px; }
  .spread--three .wordmark__name { font-size: 14px; }

  /* inner (white) card */
  .people-photo {
    position: absolute; left: 22%; right: 6%; top: 4%; height: 52%;
    background: linear-gradient(180deg, var(--photo-light) 0%, var(--photo-dark) 100%);
    border-radius: 2px;
  }
  .message {
    position: absolute; left: 16%; right: 6%; top: 64%;
    font-size: 7px; line-height: 1.3; color: var(--ink);
  }
  .swoosh { position: absolute; inset: 0; width: 100%; height: 100%; }
  .card--inner .wordmark { top: 18%; left: 58%; }
  .card--inner .wordmark__name { font-size: 17px; }
  .spread--three .card--inner .wordmark__name { font-size: 13px; }
  .contact {
    position: absolute; left: 46%; right: 4%; top: 36%;
    font-size: 7px; line-height: 1.35; color: var(--ink);
  }
  .contact__name { font-size: 10px; margin-bottom: 1px; }
  .contact__email { margin-bottom: 8px; }
  .spread--three .contact { top: 32%; font-size: 6px; }
</style>
</head>
<body>

<!-- Rosalind Pressey -->
<section class="spread spread--one">
  <div class="card card--outer">
    <div class="card__half"><div class="badge"><span class="badge__disc"></span><span class="badge__url">www.cobaltharvest-example.com</span></div></div>
    <div class="card__half"><div class="wordmark"><span class="wordmark__dot"></span><span class="wordmark__name">Cobalt Harvest</span></div></div>
  </div>
  <div class="card card--inner">
    <div class="card__half">
      <div class="people-photo" role="img" aria-label="Group of corporate business people in suits"></div>
      <p class="message">Redundant IT and Computer equipment<br>Business people - corporate business people wanted<br>All UK areas</p>
    </div>
    <div class="card__half">
      <svg class="swoosh" viewBox="0 0 100 100" preserveAspectRatio="none" aria-hidden="true">
        <path d="M0,0 L12,0 C14,45 45,82 100,84 L100,100 L0,100 Z" fill="#e6e6e6"/>
        <path d="M0,0 L8,0 C10,48 42,86 100,88 L100,100 L0,100 Z" fill="var(--green-light)"/>
        <path d="M0,0 L4,0 C6,52 38,92 100,94 L100,100 L0,100 Z" fill="var(--green)"/>
      </svg>
      <div class="wordmark"><span class="wordmark__dot"></span><span class="wordmark__name">Cobalt Harvest</span></div>
      <div class="contact">
        <p class="contact__name">Rosalind Pressey - Director</p>
        <p class="contact__email">rosalind@cobaltharvest-example.com</p>
        <p>14 Brindle Lane<br>Oakhurst Trading Park<br>Fenwick Cross<br>Herts<br>HP9 3QL<br>United Kingdom</p>
      </div>
    </div>
  </div>
</section>

<!-- Gord Pressey -->
<section class="spread spread--two">
  <div class="card card--outer">
    <div class="card__half"><div class="badge"><span class="badge__disc"></span><span class="badge__url">www.cobaltharvest-example.com</span></div></div>
    <div class="card__half"><div class="wordmark"><span class="wordmark__dot"></span><span class="wordmark__name">Cobalt Harvest</span></div></div>
  </div>
  <div class="card card--inner">
    <div class="card__half">
      <div class="people-photo" role="img" aria-label="Group of corporate business people in suits"></div>
      <p class="message">Redundant IT and Computer equipment<br>Business people - corporate business people wanted<br>All UK areas</p>
    </div>
    <div class="card__half">
      <svg class="swoosh" viewBox="0 0 100 100" preserveAspectRatio="none" aria-hidden="true">
        <path d="M0,0 L12,0 C14,45 45,82 100,84 L100,100 L0,100 Z" fill="#e6e6e6"/>
        <path d="M0,0 L8,0 C10,48 42,86 100,88 L100,100 L0,100 Z" fill="var(--green-light)"/>
        <path d="M0,0 L4,0 C6,52 38,92 100,94 L100,100 L0,100 Z" fill="var(--green)"/>
      </svg>
      <div class="wordmark"><span class="wordmark__dot"></span><span class="wordmark__name">Cobalt Harvest</span></div>
      <div class="contact">
        <p class="contact__name">Gord Pressey - Director</p>
        <p class="contact__email">gord@cobaltharvest-example.com</p>
        <p>14 Brindle Lane<br>Oakhurst Trading Park<br>Fenwick Cross<br>Herts<br>HP9 3QL<br>United Kingdom</p>
      </div>
    </div>
  </div>
</section>

<!-- Company card -->
<section class="spread spread--three">
  <div class="card card--outer">
    <div class="card__half"><div class="badge"><span class="badge__disc"></span><span class="badge__url">www.cobaltharvest-example.com</span></div></div>
    <div class="card__half"><div class="wordmark"><span class="wordmark__dot"></span><span class="wordmark__name">Cobalt Harvest</span></div></div>
  </div>
  <div class="card card--inner">
    <div class="card__half">
      <div class="people-photo" role="img" aria-label="Group of corporate business people in suits"></div>
      <p class="message">Redundant IT and Computer equipment<br>Business people - corporate business people wanted<br>All UK areas</p>
    </div>
    <div class="card__half">
      <svg class="swoosh" viewBox="0 0 100 100" preserveAspectRatio="none" aria-hidden="true">
        <path d="M0,0 L12,0 C14,45 45,82 100,84 L100,100 L0,100 Z" fill="#e6e6e6"/>
        <path d="M0,0 L8,0 C10,48 42,86 100,88 L100,100 L0,100 Z" fill="var(--green-light)"/>
        <path d="M0,0 L4,0 C6,52 38,92 100,94 L100,100 L0,100 Z" fill="var(--green)"/>
      </svg>
      <div class="wordmark"><span class="wordmark__dot"></span><span class="wordmark__name">Cobalt Harvest</span></div>
      <div class="contact">
        <p>14 Brindle Lane<br>Oakhurst Trading Park<br>Fenwick Cross<br>Herts<br>HP9 3QL<br>United Kingdom</p>
      </div>
    </div>
  </div>
</section>

</body>
</html>
```